Wordpress Design for Interactive Marketing Agency

We are looking to have a WP theme designed for our company, Bright Harbor Media. We are an online marketing firm specializing in SEO, Paid Search/PPC, Analytics and a number of other marketing channels.
We have a logo and tag line. We also have a rough and unloved design to work from as a way to illustrate the content needs of the homepage. We would like an interactive slider on the homepage which displays text and image content describing our services and our value props/solution positioning. Layering content is also something we'd like to incorporate in a block or two on the page, whether it be tabs, window shades, rotating or mouse-over type div swapping, scrolling news box, etc.
The design also needs to be able to transition to a less portal-like feel (re: the homepage) to a page design that houses a description for each of our services, an about page, privacy page, etc.
So, in the spirit of the typical WP construct, there would be a consistent header and footer, with a main content div that is flexible and eye-catching.
Three column design for the homepage feels right, but that's not a requirement. For the rest of the pages one or two columns seems like the right layout. Again, is this open to design.
To see what we've put together as a concept visit this page:
www.brightharbormedia.example/design/
Notes: most folks didn't care for the opaque gun in the background. Though, a subtle, muted background image would be a welcome design element. Keep in mind that these images are only for illustrating the content needs. We are not expecting anything that looks like these concepts. In fact, they didn't appeal to most of us.
Also included is a third design that we kind of liked (probably could live without the page curls, though). Modern sophistication that isn't stuffy but doesn't get too juvenile is what we're wanting. If there's a way to complement the power colors of our logo and attain a style that's lively, digerati in spirit and alluring, then that's what we would like to arrive at.
To get the latest logo:
http://brightharbormedia.example/design/Logo-Rework.png
The logo can be rearranged as needed.
I have also attached the rough designs we put together and the logo.
We really don't have any strong restrictions or absolutes as far as how the design turns out. We just want something that looks great and captures the spirit of the business/brand. The visuals could definitely benefit from a human element, or a splashy graphic or something festive, technically inclined and/or inclusive.
Updates
Project Deadline Extended
Reason: I am trying to make the project a little more accessible for designers by extending it a bit. I realize that the process can sometimes take several days, and if this allows for more submissions, there are no complaints here.
Hi Designers,
Target Market(s)
Medium-sized, regional businesses
Industry/Entity Type
Marketing
Requirements
Must have
- Theme must accomodate widgets, permalinks and all of the common WP page enhancements and taxonomy options.
Nice to have
- Most of the text on the page should be true text if possible (for SEO purposes, etc.). The ability to layer text content is also desirable, so having content blocks that use z-indexed divs would be ideal. Theme should accommodate widgets, permalinks and all of the common WP page enhancements and taxonomy options.

```html
<!DOCTYPE html>
<html lang="en">
<head>
<meta charset="utf-8">
<title>Bright Harbor Media — Online Marketing</title>
<link href="https://fonts.googleapis.com/css2?family=Ubuntu:wght@400;500;700&family=Open+Sans:wght@400;600;700&display=swap" rel="stylesheet">
<style>
:root{
  --ink:#2b2b2b;
  --muted:#666;
  --orange:#f5a300;
  --orange-light:#ffd84a;
  --red:#c81e00;
  --red-dark:#9e1400;
  --contact-outer:#e04a00;
  --contact-inner:#f08a00;
  --panel:#dcdcdc;
  --footer:#1c1c1c;
  --field:#fffbe8;
  --badge:#d9ecf8;
  --badge-edge:#a8cce4;
}
*{box-sizing:border-box;margin:0;padding:0}
html,body{width:1200px;height:936px;overflow:hidden;background:#fff}
body{position:relative;font-family:"Open Sans",sans-serif;color:var(--ink)}
.abs{position:absolute}

.topbar{left:460px;top:0;width:695px;height:41px;background:#1e1e1e;border-radius:0 0 8px 8px}
.topbar__cta{left:18px;top:9px;font:700 18px "Ubuntu",sans-serif;color:#fff;white-space:nowrap}
.topbar__cta .phone{color:var(--orange)}
.topbar__search{left:376px;top:8px;width:218px;height:24px;background:var(--field);border:2px solid var(--orange)}
.topbar__btn{left:607px;top:6px;width:73px;height:27px;border-radius:5px;background:linear-gradient(#e8401a,var(--red-dark));color:#fff;font:500 13px "Ubuntu",sans-serif;text-align:center;line-height:27px;border:1px solid #f0a070}

.brand{left:76px;top:96px;display:flex;align-items:center;gap:10px}
.brand__mark{width:30px;height:30px;border-radius:50%;background:var(--red)}
.brand__name{font:700 27px "Ubuntu",sans-serif;color:#222;letter-spacing:.5px}
.brand__tag{left:186px;top:138px;font:700 15px "Ubuntu",sans-serif;color:#666}

.intro{left:459px;top:66px;width:474px;height:99px;border-radius:6px;background:linear-gradient(#f6f6f6,#e2e2e2);border:1px solid #d0d0d0}
.intro__cities{left:0;top:8px;width:162px;text-align:center;font:700 17px/26px "Ubuntu",sans-serif;color:#444}
.intro__divider{left:165px;top:6px;width:8px;height:84px;background:linear-gradient(90deg,#ccc,#f4f4f4)}
.intro__text{left:185px;top:5px;width:262px;font:600 12.3px/17.5px "Open Sans",sans-serif;color:#333}

.badge{top:68px;height:97px;border-radius:3px;background:linear-gradient(#f4faff,var(--badge));border:1px solid var(--badge-edge)}
.badge--one{left:955px;width:88px}
.badge--two{left:1056px;width:97px}

.showcase{left:66px;top:193px;width:778px;height:407px;background:var(--panel);border-radius:8px}
.tab{left:79px;width:198px;height:53px;background:linear-gradient(var(--orange-light),var(--orange));border:1px solid #e08a00;font:500 20px/53px "Ubuntu",sans-serif;color:#222;padding-left:15px;text-shadow:0 1px 0 rgba(255,255,255,.4)}
.tab--active{width:214px;height:52px;background:linear-gradient(#e03810,var(--red-dark));color:#fff;border-color:#f4c000;text-shadow:none}
.tab--active::after{content:"";position:absolute;right:-16px;top:12px;border-left:16px solid #c72800;border-top:14px solid transparent;border-bottom:14px solid transparent}
.slide{left:300px;top:202px;width:533px;height:362px;background:#fff}
.slide__art{left:47px;top:5px;width:412px;height:266px;background:radial-gradient(circle at 40% 25%,#e8402a 0 9%,transparent 10%),linear-gradient(160deg,#ffffff 0%,#d6e4f2 35%,#a9c6e2 65%,#f4f4f4 100%)}
.slide__title{left:17px;top:280px;font:700 14px "Open Sans",sans-serif;color:var(--red)}
.slide__text{left:17px;top:298px;width:480px;font:600 14px/17.6px "Open Sans",sans-serif;color:var(--muted)}
.dots{left:748px;top:575px;display:flex;gap:4px}
.dots span{width:12px;height:12px;border-radius:50%;background:#8f8f8f}
.dots span.is-active{background:var(--red)}

.contact{left:868px;top:191px;width:287px;height:409px;border-radius:8px;background:linear-gradient(#d44000,var(--contact-outer) 60%,#ff6000)}
.contact__title{left:0;top:12px;width:100%;text-align:center;font:500 20px "Ubuntu",sans-serif;color:#fff}
.contact__body{left:9px;top:47px;width:269px;height:353px;border-radius:8px;background:var(--contact-inner);border:1px solid #f7b55a}
.contact__label{left:12px;font:500 18px/22px "Ubuntu",sans-serif;color:#fff}
.contact__field{left:11px;width:240px;background:var(--field);border:1px solid #d07000}
.contact__send{left:97px;top:312px;width:72px;height:31px;border-radius:5px;background:linear-gradient(#e8401a,var(--red-dark));border:1px solid #ffb060;color:#fff;font:700 15px/29px "Ubuntu",sans-serif;text-align:center}

.services{left:58px;top:632px;width:1097px;height:196px;background:linear-gradient(#2a2a2a,var(--footer))}
.services__rule{top:14px;width:1px;height:168px;background:#444}
.services__list{list-style:none;top:25px;font:700 13px/26.4px "Open Sans",sans-serif;color:#fff}
.services__thumb{top:25px;height:145px;border-radius:4px}
.thumb--phones{left:125px;width:136px;background:linear-gradient(135deg,#fafafa,#9aa3aa 55%,#e8e0c8)}
.thumb--flow{left:542px;width:141px;background:radial-gradient(circle at 50% 55%,#6d9bc7,#dce8f3 70%)}
.thumb--cloud{left:918px;width:163px;background:radial-gradient(circle,#f7f1e8 20%,#d8c7b0 70%,#a89480)}

.legal{left:66px;top:862px;font:600 13px "Open Sans",sans-serif;color:#111;display:flex;gap:15px}
.legal .sep{font-weight:400;color:#111}
.social{left:909px;top:852px;display:flex;gap:4px}
.social span{width:24px;height:24px;border-radius:3px;background:#3a7fc0}
.accredit{left:1049px;top:843px;width:106px;height:43px;border-radius:4px;background:#176b8a}
.copyright{right:45px;top:896px;font:400 12px "Open Sans",sans-serif;color:#666}
</style>
</head>
<body>

<header>
  <div class="abs topbar">
    <div class="abs topbar__cta"><span class="phone">1 800 555 0148</span> GET A FREE AUDIT!</div>
    <div class="abs topbar__search" aria-label="Search"></div>
    <div class="abs topbar__btn">SEARCH</div>
  </div>

  <div class="abs brand">
    <span class="brand__mark"></span>
    <span class="brand__name">BRIGHT HARBOR MEDIA</span>
  </div>
  <div class="abs brand__tag">Online Marketing. Made Bright.</div>

  <div class="abs intro">
    <div class="abs intro__cities">Online Marketing<br>Dallas Austin<br>Houston</div>
    <div class="abs intro__divider"></div>
    <p class="abs intro__text">Bright Harbor Media is a full-service Internet marketing agency providing Paid Search (PPC) Search Engine Optimization (SEO), Display Advertising, Analytics Consulting, Creative Direction, and....</p>
  </div>

  <div class="abs badge badge--one" role="img" aria-label="Certified partner badge"></div>
  <div class="abs badge badge--two" role="img" aria-label="Certified partner badge"></div>
</header>

<main>
  <section class="abs showcase" aria-label="Services slider"></section>
  <nav>
    <div class="abs tab tab--active" style="top:202px">PAID SEARCH</div>
    <div class="abs tab" style="top:283px">SEO</div>
    <div class="abs tab" style="top:359px">DISPLAY ADS</div>
    <div class="abs tab" style="top:435px">ANALYTICS</div>
    <div class="abs tab" style="top:510px">PERFORMANCE</div>
  </nav>
  <article class="abs slide">
    <div class="abs slide__art" role="img" aria-label="Illustration of a large red map pin over a city street map with a team holding service cards"></div>
    <h2 class="abs slide__title">ARE YOU ON THE MAP?</h2>
    <p class="abs slide__text">We can get you there with our Local SEO service. Local SEO is essential to your online marketing. We help you expand your local presense in SEO and beyond.</p>
  </article>
  <div class="abs dots"><span class="is-active"></span><span></span><span></span><span></span><span></span></div>

  <aside class="abs contact">
    <h2 class="abs contact__title">CONTACT US</h2>
    <div class="abs contact__body">
      <div class="abs contact__label" style="top:10px">Name:</div>
      <div class="abs contact__field" style="top:39px;height:29px"></div>
      <div class="abs contact__label" style="top:80px">Email:</div>
      <div class="abs contact__field" style="top:110px;height:29px"></div>
      <div class="abs contact__label" style="top:158px">How can we help you?</div>
      <div class="abs contact__field" style="top:188px;height:113px"></div>
      <div class="abs contact__send">SEND</div>
    </div>
  </aside>
</main>

<footer>
  <section class="abs services">
    <ul class="abs services__list" style="left:16px">
      <li>LOCAL SEO</li><li>LINK BUILDING</li><li>CONTENT</li><li>DESIGN</li><li>DEVELOPMENT</li><li>MOBILE</li>
    </ul>
    <div class="abs services__thumb thumb--phones" role="img" aria-label="Photo of two smartphones showing a local map"></div>
    <div class="abs services__rule" style="left:326px"></div>
    <ul class="abs services__list" style="left:362px">
      <li>ATTRIBUTION TRACKING</li><li>CALL TRACKING</li><li>PAY FOR PERFORMANCE</li><li>AFFILIATE MARKETING</li><li>RETARGETING</li><li>LANDING PAGE TESTING</li>
    </ul>
    <div class="abs services__thumb thumb--flow" role="img" aria-label="Diagram of marketing channels feeding into call tracking"></div>
    <div class="abs services__rule" style="left:744px"></div>
    <ul class="abs services__list" style="left:771px">
      <li>SOCIAL MEDIA</li><li>VIDEO COMMERCE</li><li>CUSTOM ANALYTICS</li><li>CUSTOM REPORTING</li><li>RETARGETING</li>
    </ul>
    <div class="abs services__thumb thumb--cloud" role="img" aria-label="Word cloud about social media"></div>
  </section>

  <nav class="abs legal">
    <span>Privacy Policy</span><span class="sep">|</span>
    <span>Terms of Service</span><span class="sep">|</span>
    <span>About Us</span><span class="sep">|</span>
    <span>Contact Us</span><span class="sep">|</span>
    <span>Our Blog</span>
  </nav>
  <div class="abs social" aria-label="Social links"><span></span><span></span><span></span></div>
  <div class="abs accredit" role="img" aria-label="Business accreditation badge"></div>
  <p class="abs copyright">© Copyright 2012 Bright Harbor Media, LLC</p>
</footer>

</body>
</html>
```